Venture firm needs flyer to attract Sales Professionals as Advisors

Creation of either a pdf Flyer or Brochure.
The target audience are senior sales professionals of the Information Technology industry. The flyer needs to come across highly professional, business oriented, positive. Text for the brochure is attached. The colors/graphics should align with Brindmore Capital corporate appearance: www.brindmore.capital

Target Market(s)

Sales Professionals in the Information Technology Industry

Industry/Entity Type

Information Technology

Font styles to use
• Raleway

Requirements
Must have
• fitting the corporate look and feel: www.brindmore.capital

```html
<!DOCTYPE html>
<html lang="en">
<head>
<meta charset="utf-8">
<title>Brindmore Capital – How it works</title>
<link rel="stylesheet" href="https://fonts.googleapis.com/css2?family=Raleway:wght@400;500;700&display=swap">
<style>
  :root {
    --page-bg: #ffffff;
    --flyer-blue: #3b6f9a;
    --label-bg: #d3dde8;
    --bar-bg: #8aaac4;
    --heading-navy: #123a5e;
    --body-text: #f2f5f8;
  }
  html, body {
    margin: 0;
    padding: 0;
    width: 1200px;
    height: 1000px;
    overflow: hidden;
    background: var(--page-bg);
    font-family: "Raleway", sans-serif;
  }
  .canvas {
    position: relative;
    width: 1200px;
    height: 1000px;
  }
  .flyer {
    position: absolute;
    left: 302px;
    top: 79px;
    width: 595px;
    height: 842px;
    background: var(--flyer-blue);
  }
  .section-bar {
    position: absolute;
    left: 0;
    width: 595px;
    height: 37px;
    background: var(--bar-bg);
  }
  .section-label {
    position: absolute;
    left: 0;
    top: 0;
    width: 176px;
    height: 37px;
    background: var(--label-bg);
  }
  .section-title {
    position: absolute;
    top: 0;
    margin: 0;
    line-height: 38px;
    font-size: 20px;
    font-weight: 700;
    color: var(--heading-navy);
    white-space: nowrap;
  }
  .body-copy {
    position: absolute;
    margin: 0;
    font-size: 11px;
    line-height: 14.4px;
    font-weight: 400;
    color: var(--body-text);
  }
  .body-copy + .body-copy { margin-top: 0; }
  .photo {
    position: absolute;
    top: 485px;
    width: 170px;
    height: 249px;
  }
  .photo--climber {
    left: 32px;
    background: linear-gradient(180deg, #4a3520 0%, #6b5530 30%, #c9b460 65%, #e8d98a 85%, #b99c4f 100%);
  }
  .photo--lake {
    left: 213px;
    background: linear-gradient(180deg, #f0e8ee 0%, #e6dfe6 40%, #5f7d78 60%, #3fa3a6 80%, #2c6f72 100%);
  }
  .photo--skier {
    left: 394px;
    background: linear-gradient(160deg, #e9ebee 0%, #dfe2e6 50%, #f3f4f6 100%);
  }
  .footer-band {
    position: absolute;
    left: 0;
    top: 804px;
    width: 595px;
    height: 8px;
    background: var(--label-bg);
  }
</style>
</head>
<body>
<div class="canvas">
  <article class="flyer">

    <div class="section-bar" style="top:49px;">
      <div class="section-label"></div>
      <h2 class="section-title" style="left:36px;">How it works</h2>
    </div>
    <div class="body-copy" style="left:36px; top:93px; width:530px;">
      <p style="margin:0;">BSC members will be introduced to Brindmore Capital’ client and portfolio companies. This unique ability to learn about latest technology innovation keeps the participants up to date with industry trends and could open interesting earning or employment opportunities.</p>
      <p style="margin:14px 0 0;">Once exposed to a specific vendor, BSC members can decide if and how they would like to get further involved. Dependent on the interest level for the specific technology, the ability to offer a solution to a known customer problem or the sheer interest to develop new business, BSC members can participate in two ways:</p>
    </div>

    <div class="section-bar" style="top:238px;">
      <div class="section-label"></div>
      <h2 class="section-title" style="left:33px;">As Associates</h2>
    </div>
    <p class="body-copy" style="left:33px; top:290px; width:480px;">Associates are actively selling and promoting one or more Brindmore Capital` portfolio companies. This could be an employment or a freelance opportunity.</p>

    <div class="section-bar" style="top:358px;">
      <div class="section-label"></div>
      <h2 class="section-title" style="left:27px;">As Advisors</h2>
    </div>
    <p class="body-copy" style="left:27px; top:403px; width:540px;">Advisors offer their contacts and knowledge about customers to Associates.<br>Advisors could create leads, support with introductions, explain customer organization and processes etc. They will be compensated by Associates with a pre-negotiated % of commission of a future sale that was supported by the Advisor.</p>

    <div class="photo photo--climber" role="img" aria-label="Photo: silhouette of a rock climber hanging from an overhang against a golden sky"></div>
    <div class="photo photo--lake" role="img" aria-label="Photo: person standing on a rock looking over a turquoise mountain lake"></div>
    <div class="photo photo--skier" role="img" aria-label="Photo: skier in a red jacket carving through fresh snow"></div>

    <p class="body-copy" style="left:32px; top:748px; width:510px;">Whatever level of involvement a BSC member seeks there is plenty of opportunity to be rewarded for working with fellow Sales Professionals and Great Startups on the forefront of technical innovation.</p>

    <div class="footer-band"></div>
  </article>
</div>
</body>
</html>
```